Letterbox drop flyer

We are looking for some designs for some A5 flyers back to back in colour. We would like one side aimed at attracting people for home loans and the other side car loans. We would like to have one side aimed at home loans and re-financing and the other side aimed at car loans.
Somewhere on both pages in a speech bubble or a star or something creative have (New office is located on the ground floor, 47 Quenby St Marlowe) as we are looking to hit our local community
We have a special offer to go on each side. On the home loans side, $100 extra cash in the customers hand if we can't find them a better mortgage product. On the car loans side we have 3 years of free roadside assistance with every loan settled with Brightway Finance Partners.
We would like to see designs with the same colours of our logo, blue and while with a professional crisp feel to it.
We want something that is going to be creative and capture the attention of our customer when they first look at it and want to read on.
We have more information on our website regarding our services and different types of home loans and vehicle loans.
We would like it to have our contac details:
Ph: 1300 418 563
www.brightwayfinancepartners.com.au
Like us on facebook: www.facebook.com/brightwayfinancepartners
Please feel free to email me with any questions
Target Market(s)
Anyone over the age of 18 looking for a car loan or home loan
Industry/Entity Type
Loan

```html
<!DOCTYPE html>
<html lang="en">
<head>
<meta charset="utf-8">
<title>Brightway Finance Partners – Letterbox Flyer</title>
<link href="https://fonts.googleapis.com/css2?family=Roboto:wght@300;400;700;900&display=swap" rel="stylesheet">
<style>
  :root {
    --page-bg: #0e1a2c;
    --paper: #ffffff;
    --brand-blue: #2ba3dc;
    --strip-blue: #5cbfe9;
    --office-red: #c8213a;
    --ink: #1c1c1c;
    --muted: #555c63;
    --bubble: rgba(150, 156, 160, 0.55);
    --bubble-text: #f4f6f7;
    --burst-orange: #ee5a24;
    --burst-red: #b3192b;
  }
  * { box-sizing: border-box; margin: 0; padding: 0; }
  html, body { width: 1200px; height: 817px; overflow: hidden; }
  body {
    background: var(--page-bg);
    font-family: "Roboto", Arial, sans-serif;
    position: relative;
  }
  .flyer {
    position: absolute;
    top: 58px;
    width: 520px;
    height: 700px;
    background: var(--paper);
    overflow: hidden;
  }
  .flyer--car { left: 50px; }
  .flyer--home { left: 630px; }

  .flyer__header {
    position: absolute; left: 0; top: 0; width: 100%; height: 130px;
    display: flex; align-items: center; padding: 0 22px;
    background: var(--paper);
  }
  .brand { display: flex; align-items: center; gap: 10px; width: 290px; }
  .brand__mark { width: 34px; height: 34px; background: var(--brand-blue); flex: none; }
  .brand__name {
    color: var(--brand-blue); font-weight: 400; font-size: 27px; line-height: 1.05;
  }
  .office {
    border-left: 2px solid #c9ccd0; padding-left: 10px; height: 86px;
    display: flex; flex-direction: column; justify-content: center;
  }
  .office__title { color: var(--office-red); font-size: 22px; font-weight: 400; line-height: 1; }
  .office__address { color: var(--muted); font-size: 11px; line-height: 1.25; margin-top: 3px; }
  .social { display: flex; align-items: center; gap: 6px; margin-top: 8px; }
  .social__square { width: 18px; height: 18px; background: #3b5a9a; }
  .social__handle { font-size: 10px; color: var(--muted); }

  .contact-strip {
    position: absolute; left: 0; top: 130px; width: 100%; height: 12px;
    background: var(--strip-blue);
  }
  .contact-strip__phone {
    position: absolute; left: 22px; top: -2px; height: 14px; padding: 0 8px;
    background: var(--strip-blue); color: #fff; font-size: 10px; line-height: 14px;
  }
  .contact-strip__web {
    position: absolute; right: 22px; top: -14px; font-size: 10px; color: var(--muted);
  }

  .photo { position: absolute; left: 0; top: 142px; width: 100%; height: 548px; }
  .photo--car {
    background: linear-gradient(160deg, #f2f4f5 0%, #e3e6e8 35%, #cfd4d8 60%, #dfe2e4 100%);
  }
  .photo--home {
    background: linear-gradient(180deg, #d8ecf7 0%, #eaf3f8 40%, #e6e8e6 65%, #cfd8cc 100%);
  }
  .bottom-band {
    position: absolute; left: 0; bottom: 0; width: 100%; height: 10px; background: var(--strip-blue);
  }

  .headline { position: absolute; color: var(--ink); font-weight: 300; line-height: 1; }
  .headline__sub { display: block; font-size: 9.5px; font-weight: 400; color: var(--muted); margin-top: 2px; }

  .bubble {
    position: absolute; background: var(--bubble); color: var(--bubble-text);
    font-size: 10px; line-height: 1.3; padding: 12px 14px;
  }
  .bubble::before {
    content: ""; position: absolute; left: 0; top: -12px;
    border-left: 14px solid var(--bubble); border-top: 12px solid transparent;
  }

  .burst { position: absolute; width: 240px; height: 240px; }
  .burst svg { position: absolute; inset: 0; width: 100%; height: 100%; }
  .burst__text {
    position: absolute; inset: 0; display: flex; flex-direction: column;
    align-items: center; justify-content: center; color: #fff; text-align: center; line-height: 1;
  }

  .offer-roadside .lead { font-size: 30px; font-weight: 400; }
  .offer-roadside .big { font-size: 54px; font-weight: 900; letter-spacing: 1px; }
  .offer-roadside .small { font-size: 11px; margin-top: 10px; }

  .offer-cash .big { font-size: 66px; font-weight: 900; }
  .offer-cash .big sup { font-size: 36px; vertical-align: 22px; }
  .offer-cash .mid { font-size: 20px; font-weight: 900; }
  .offer-cash .mid span { font-weight: 400; }
  .offer-cash .small { font-size: 11px; font-weight: 700; margin-top: 3px; }
  .offer-cash .tiny { font-size: 9px; margin-top: 1px; }

  .cash-photo {
    position: absolute; left: 285px; top: 430px; width: 215px; height: 265px;
    background: linear-gradient(150deg, #d9dfd2 0%, #b9c3ae 50%, #8f9c86 100%);
    transform: rotate(-6deg);
  }
  .bad-credit { position: absolute; left: 26px; top: 272px; width: 230px; color: var(--ink); }
  .bad-credit__ask { font-size: 15px; font-weight: 300; line-height: 1.2; }
  .bad-credit__call { font-size: 21px; font-weight: 400; margin-top: 6px; }
  .bad-credit__note { font-size: 10px; color: var(--muted); line-height: 1.2; }
</style>
</head>
<body>

<section class="flyer flyer--car">
  <div class="photo photo--car" role="img" aria-label="Close-up of a white car's rear light and wheel, softly faded"></div>

  <header class="flyer__header">
    <div class="brand">
      <span class="brand__mark"></span>
      <span class="brand__name">Brightway Finance Partners</span>
    </div>
    <div class="office">
      <p class="office__title">NEW OFFICE</p>
      <p class="office__address">is located on the ground floor,<br>47 Quenby St Marlowe</p>
      <div class="social"><span class="social__square"></span><span class="social__handle">brightwayfinancepartners</span></div>
    </div>
  </header>
  <div class="contact-strip">
    <span class="contact-strip__phone">Ph: 1300 418 563</span>
    <span class="contact-strip__web">www.brightwayfinancepartners.com.au</span>
  </div>

  <h1 class="headline" style="left:22px;top:180px;font-size:36px;">CAR LOAN!
    <span class="headline__sub">Home Loan &amp; Mortgage Brokers Australia Wide!</span></h1>

  <p class="bubble" style="left:22px;top:252px;width:250px;">"We will show you the loan the bank forgot to mention" Brightway Finance Partners offer home loans tailored to your needs from a range of Australia's top Banks and lenders. We can provide finance for property transactions ranging from the simple to the complex. The best part is our service is completely FREE to you.</p>

  <div class="burst offer-roadside" style="left:12px;top:476px;">
    <svg viewBox="-100 -100 200 200" aria-hidden="true"><polygon fill="var(--burst-orange)" points="100,0 85,22.8 86.6,50 62.2,62.2 50,86.6 22.8,85 0,100 -22.8,85 -50,86.6 -62.2,62.2 -86.6,50 -85,22.8 -100,0 -85,-22.8 -86.6,-50 -62.2,-62.2 -50,-86.6 -22.8,-85 0,-100 22.8,-85 50,-86.6 62.2,-62.2 86.6,-50 85,-22.8"/></svg>
    <div class="burst__text">
      <span class="lead">3 years of</span>
      <span class="big">FREE</span>
      <span class="small">ROADSIDE ASSISTANCE</span>
    </div>
  </div>
  <div class="bottom-band"></div>
</section>

<section class="flyer flyer--home">
  <div class="photo photo--home" role="img" aria-label="Blurred suburban house under a pale blue sky"></div>

  <header class="flyer__header">
    <div class="brand">
      <span class="brand__mark"></span>
      <span class="brand__name">Brightway Finance Partners</span>
    </div>
    <div class="office">
      <p class="office__title">NEW OFFICE</p>
      <p class="office__address">is located on the ground floor,<br>47 Quenby St Marlowe</p>
      <div class="social"><span class="social__square"></span><span class="social__handle">brightwayfinancepartners</span></div>
    </div>
  </header>
  <div class="contact-strip">
    <span class="contact-strip__phone">Ph: 1300 418 563</span>
    <span class="contact-strip__web">www.brightwayfinancepartners.com.au</span>
  </div>

  <h1 class="headline" style="left:26px;top:166px;font-size:24px;">HOME LOAN<br>OPTIONS
    <span class="headline__sub">Home Loan &amp; Mortgage Brokers Australia Wide!</span></h1>

  <p class="bubble" style="left:250px;top:168px;width:225px;">"We will show you the loan the bank forgot to mention" Brightway Finance Partners offer home loans tailored to your needs from a range of Australia's top Banks and lenders. We can provide finance for property transactions ranging from the simple to the complex. The best part is our service is completely FREE to you.</p>

  <div class="bad-credit">
    <p class="bad-credit__ask">BAD CREDIT? WANT A<br>CAR LOAN?</p>
    <p class="bad-credit__call">LET US HELP!</p>
    <p class="bad-credit__note">Car Loans For Bad Credit Customers Are Available Today - Get A Car Loan With Bad Credit!</p>
  </div>

  <p class="bubble" style="left:252px;top:306px;width:210px;">Bad Credit Car Loans offer customers the ability to get the car they want with access to Australia's leading banks and lending institutions as well as national and international private lenders that cater specifically for people with bad credit or who have been credit impaired in the past.</p>

  <div class="cash-photo" role="img" aria-label="Fanned banknotes"></div>

  <div class="burst offer-cash" style="left:-6px;top:470px;">
    <svg viewBox="-100 -100 200 200" aria-hidden="true"><polygon fill="var(--burst-red)" points="100,0 85,22.8 86.6,50 62.2,62.2 50,86.6 22.8,85 0,100 -22.8,85 -50,86.6 -62.2,62.2 -86.6,50 -85,22.8 -100,0 -85,-22.8 -86.6,-50 -62.2,-62.2 -50,-86.6 -22.8,-85 0,-100 22.8,-85 50,-86.6 62.2,-62.2 86.6,-50 85,-22.8"/></svg>
    <div class="burst__text">
      <span class="big"><sup>$</sup>100</span>
      <span class="mid">EXTRA <span>CASH</span></span>
      <span class="small">in the your hand</span>
      <span class="tiny">if we can't find a<br>better mortgage product.</span>
    </div>
  </div>
  <div class="bottom-band"></div>
</section>

</body>
</html>
```